Financial Advisor Business Card

This business card is mainly a card for me personally (Marcus Pellinger) providing services as a Financial Planner and Accountant. My title is: Worth.wise Planner
Details provided about Harbour Financial Planners on the reverse side of the card is not dominant information, it is provided for ease of contact/communication purposes for prospective clients.
About me: I provide financial advice to my clients however due to regulatory issues in my industry I cannot use the title "Financial Advisor".
Target market is 25 y/o and onwards projecting a cutting edge, innovative and modern marketing influence.
Target Market(s)
25 years old and older
Industry/Entity Type
Financial
Contact Information for Business Card
Front side of business card
Name: Marcus Pellinger
Position: Worth.wise Planner
Accreditations:
Dip FS(FP)
B.Comm
Mobile: 0438 702 519
e-mail: mp@harbourfp.example.au
website: www.harbourfp.example.au
Reverse side of business card
Name: Marcus Pellinger
Company: Harbour Financial Planners
Position: Senior Accountant
Address:
Level 6, Suite 4
47 Orwell Road
PO Box 817
MERRIVALE NSW 2315
Phone: (02) 49581737
Requirements
Must have
- - Cutting edge, innovative, fun but professional, modern marketing design and fonts
- Professional and legible
- Futuristic sharp lines, some with rounded edges
- Preferred Front Card colour scheme: Black background, Silver Text, White Text, Red & Silver lines
- Preferred Reverse Card colour scheme: White background, Silver Text, Black Text, Aqua & Silver lines
Nice to have
- Design a cutting edge logo of my intials as capital letters: MP
with a bigger D and smaller K - Preferred colour is Silver Text
Should not have
- Must not be:
- vintage/classic
- stereotypical accountant/tax agent/money style business card
- old style fonts e.g. times new roman

```html
<!DOCTYPE html>
<html lang="en">
<head>
<meta charset="utf-8">
<title>Marcus Pellinger – Business Card</title>
<link rel="stylesheet" href="https://fonts.googleapis.com/css2?family=Open+Sans:wght@400;600;700&family=Questrial&display=swap">
<style>
  :root {
    --page-bg: #e9e6e1;
    --red-deep: #7c0f16;
    --red: #a81c26;
    --red-light: #c3313a;
    --silver: #a7a7a9;
    --silver-light: #dcdcdd;
    --white: #ffffff;
    --text-light: #f3eaea;
  }
  * { box-sizing: border-box; margin: 0; padding: 0; }
  html, body {
    width: 1200px; height: 1024px; overflow: hidden;
    background: var(--page-bg);
    font-family: "Open Sans", Arial, sans-serif;
  }
  .sheet { position: relative; width: 1200px; height: 1024px; }
  .card {
    position: absolute; left: 194px; width: 812px; height: 464px;
    overflow: hidden;
    box-shadow: 0 10px 28px rgba(0,0,0,0.22);
  }
  .card--front { top: 30px; }
  .card--back {
    top: 530px;
    background: linear-gradient(160deg, var(--red-deep) 0%, var(--red) 55%, var(--red-light) 100%);
  }
  .card-shape { position: absolute; inset: 0; width: 100%; height: 100%; }

  .monogram {
    position: absolute; left: 96px; top: 130px;
    font-family: "Questrial", sans-serif;
    font-size: 168px; line-height: 1; letter-spacing: -4px;
    color: var(--red);
    white-space: nowrap;
  }

  .contact-list {
    position: absolute; right: 40px; top: 40px;
    list-style: none; color: var(--white);
    font-family: "Questrial", sans-serif; font-size: 21px;
  }
  .contact-list li { display: flex; align-items: center; gap: 12px; margin-bottom: 9px; white-space: nowrap; }
  .contact-list svg { width: 16px; height: 16px; flex: none; }

  .divider {
    position: absolute; left: 604px; top: 232px; width: 70px; height: 2px;
    background: var(--silver-light); transform: rotate(28deg);
  }

  .identity { position: absolute; left: 472px; bottom: 44px; color: var(--white); }
  .identity__name { font-weight: 700; font-size: 25px; letter-spacing: 0.2px; }
  .identity__title, .identity__creds {
    font-family: "Questrial", sans-serif; font-size: 20px; color: var(--text-light); margin-top: 3px;
  }

  .company-name {
    position: absolute; right: 56px; top: 70px; width: 460px;
    font-family: "Questrial", sans-serif; font-size: 44px; line-height: 1.15;
    letter-spacing: 3px; text-transform: uppercase; text-align: right;
    color: var(--silver-light);
  }
  .back-details {
    position: absolute; left: 46px; right: 46px; bottom: 60px;
    color: var(--white); font-size: 17px; line-height: 1.75;
    font-family: "Questrial", sans-serif;
  }
  .back-details__person { font-family: "Open Sans", sans-serif; font-weight: 700; font-size: 19px; }
</style>
</head>
<body>
<main class="sheet">

  <section class="card card--front" aria-label="Business card front">
    <svg class="card-shape" viewBox="0 0 812 464" preserveAspectRatio="none" aria-hidden="true">
      <defs>
        <linearGradient id="paperGrad" x1="0" y1="0" x2="1" y2="1">
          <stop offset="0" stop-color="#f0f0f0"/>
          <stop offset="0.5" stop-color="#ffffff"/>
          <stop offset="1" stop-color="#dcdcdc"/>
        </linearGradient>
        <linearGradient id="redGrad" x1="0" y1="0" x2="1" y2="1">
          <stop offset="0" stop-color="#c3313a"/>
          <stop offset="0.6" stop-color="#a81c26"/>
          <stop offset="1" stop-color="#7c0f16"/>
        </linearGradient>
      </defs>
      <rect width="812" height="464" fill="url(#paperGrad)"/>
      <path d="M430 0 Q 330 240 440 464 L812 464 L812 0 Z" fill="#a7a7a9"/>
      <path d="M452 0 Q 352 240 462 464 L812 464 L812 0 Z" fill="url(#redGrad)"/>
    </svg>

    <div class="monogram">MP</div>

    <ul class="contact-list">
      <li>
        <svg viewBox="0 0 16 16" aria-hidden="true"><rect x="4" y="1" width="8" height="14" rx="1.5" fill="none" stroke="#fff" stroke-width="1.6"/><circle cx="8" cy="12.3" r="0.9" fill="#fff"/></svg>
        0438 702 519
      </li>
      <li>
        <svg viewBox="0 0 16 16" aria-hidden="true"><rect x="1" y="3" width="14" height="10" rx="1" fill="#fff"/><path d="M1.5 3.5 L8 9 L14.5 3.5" fill="none" stroke="#a81c26" stroke-width="1.3"/></svg>
        mp@harbourfp.example.au
      </li>
      <li>
        <svg viewBox="0 0 16 16" aria-hidden="true"><circle cx="8" cy="8" r="6.6" fill="none" stroke="#fff" stroke-width="1.4"/><ellipse cx="8" cy="8" rx="2.8" ry="6.6" fill="none" stroke="#fff" stroke-width="1.1"/><path d="M1.5 8 H14.5" stroke="#fff" stroke-width="1.1"/></svg>
        www.harbourfp.example.au
      </li>
    </ul>

    <div class="divider" aria-hidden="true"></div>

    <div class="identity">
      <p class="identity__name">Marcus Pellinger</p>
      <p class="identity__title">Worth.wise Planner</p>
      <p class="identity__creds">Dip FS(FP) | B.Comm</p>
    </div>
  </section>

  <section class="card card--back" aria-label="Business card back">
    <p class="company-name">Harbour Financial Planners</p>
    <div class="back-details">
      <p><span class="back-details__person">Marcus Pellinger | Senior Accountant</span></p>
      <p>a: Level 6, Suite 4 47 Orwell Road PO Box 817 MERRIVALE NSW 2315</p>
      <p>p: (02) 49581737 | e: mp@harbourfp.example.au | w: www.harbourfp.example.au</p>
    </div>
  </section>

</main>
</body>
</html>
```